Web design for Marketplace

Guys!
1st of all, thank you for willing to help me out.
I have attached PDF file with examples.
I am looking for professional and clean design for my new project “ Lantern of Seers “. Its marketplace for Psychic Readers around the world. Where they will able to register to provide their services via Chat,Email and sell their products on their personal stores.
Customer will able to get services and buy products from Psychic on Marketplace.
url : http://www.lanternofseers-demo.net
Please note: it doesn’t matter, what my current site looks like. I am looking for completely new design.
It doesn't matter if you add or remove : Clipvale video or even text which is on the home page in new design.
Following are the main pages of the website, which i am looking to be design.
1. Home page
2. Psychic
3. Marketplace
4. Psychic profile page
5. Psychic Store page
6. Psychic product page
7. Logo
following is the website, which i like the most. I would love to have something like that. It is neat , clean and friendly. I am looking for depth in design and neatness and borders (matter and a lot and it should be prefect ).
http://www.craftnook-demo.net
P.S : i believe it will be helpful to choose one of you. If you can only create design of " Homepage" at 1st , so i can go ahead and hire one of you guys.
Best,
Hi guys!
Guys,

```html
<!DOCTYPE html>
<html lang="en">
<head>
<meta charset="utf-8">
<title>Lantern of Seers — Home</title>
<link href="https://fonts.googleapis.com/css2?family=Oswald:wght@400;500&family=Roboto+Condensed:wght@400;700&family=Roboto:wght@400&display=swap" rel="stylesheet">
<style>
:root{
  --orange:#f2621a;
  --orange-deep:#e4520b;
  --orange-light:#f77a30;
  --ink:#3a3a3a;
  --grey-text:#5c5c5c;
  --grey-head:#5a5a5a;
  --line:#d6d6d6;
  --page:#eeeeee;
  --white:#ffffff;
  --footer:#3b3b3b;
}
*{box-sizing:border-box;margin:0;padding:0}
html,body{width:1024px;height:1200px;overflow:hidden}
body{position:relative;background:linear-gradient(#ffffff 0,#f3f3f3 110px,#ececec 520px,#f1f1f1 1150px);font-family:"Roboto",sans-serif;color:var(--ink)}
.abs{position:absolute}

/* header */
.brand{left:112px;top:22px}
.brand-name{font-family:"Oswald",sans-serif;font-weight:500;font-size:34px;line-height:40px;color:#1e1e1e;letter-spacing:.5px}
.brand-tag{font-family:"Roboto",sans-serif;font-size:19px;color:#333;margin-top:6px}
.main-nav{right:112px;top:14px;font-family:"Roboto Condensed",sans-serif;font-size:14px;color:#555;display:flex;gap:9px;align-items:center}
.main-nav span.sep{width:1px;height:10px;background:#999}
.search{left:521px;top:50px;width:391px;height:27px;display:flex;gap:4px}
.search-field{flex:1;border:1px solid #cfcfcf;background:#fff;box-shadow:inset 0 1px 2px rgba(0,0,0,.12);font-family:"Roboto Condensed",sans-serif;font-style:italic;font-size:11px;color:#bbb;padding:7px 8px}
.search-btn{width:76px;background:linear-gradient(var(--orange-light),var(--orange-deep));color:#fff;font-family:"Oswald",sans-serif;font-size:15px;text-align:center;line-height:27px}

/* hero */
.hero{left:0;top:120px;width:1024px;height:377px;border-top:2px solid #8a8a8a;border-bottom:3px solid var(--orange);background:linear-gradient(100deg,#c9b6a4 0%,#e8d6c3 25%,#b9b9bf 50%,#dcc6ae 70%,#a8aab3 100%)}
.hero-banner{left:0;top:249px;width:532px;height:109px;background:rgba(242,98,26,.93)}
.hero-kicker{left:112px;top:256px;font-family:"Oswald",sans-serif;font-size:36px;line-height:44px;color:#1a1a1a;letter-spacing:-1px}
.hero-title{left:110px;top:292px;font-family:"Oswald",sans-serif;font-size:50px;line-height:60px;color:#fff;letter-spacing:-1px}

/* welcome */
.welcome{left:112px;top:507px;width:620px;height:136px;background:#fff;border:1px solid #e2e2e2;box-shadow:0 4px 8px rgba(0,0,0,.08);padding:16px 15px}
.welcome h1{font-family:"Oswald",sans-serif;font-weight:400;font-size:20px;color:var(--grey-head);padding-bottom:6px;border-bottom:1px solid #cfcfcf;width:520px}
.welcome p{font-size:8.6px;line-height:12px;color:#444;width:530px;margin-top:7px}
.orange-side{left:640px;top:507px}
.join-title{left:760px;top:520px;width:150px;text-align:center;font-family:"Oswald",sans-serif;color:#fff;font-size:34px;line-height:38px;letter-spacing:-1px}
.btn-light{background:linear-gradient(#ffffff,#e2e2e2);border:1px solid #cfcfcf;font-family:"Oswald",sans-serif;color:#555;text-align:center}
.join-btn{left:782px;top:603px;width:112px;height:24px;font-size:14px;line-height:22px}
.mails-title{left:656px;top:673px;font-family:"Oswald",sans-serif;font-size:20px;color:#fff}
.mails-rule{left:656px;top:713px;width:240px;height:1px;background:rgba(255,255,255,.5)}
.mails-sub{left:660px;top:723px;width:240px;font-family:"Roboto Condensed",sans-serif;font-weight:700;font-size:15px;line-height:19px;color:#fff}
.mails-field{left:659px;top:776px;width:237px;height:30px;background:#fff;font-family:"Roboto Condensed",sans-serif;font-size:12px;color:#aaa;padding:8px 8px}
.mails-btn{left:821px;top:815px;width:74px;height:25px;font-size:14px;line-height:23px}

/* products */
.products-title{left:112px;top:673px;font-family:"Oswald",sans-serif;font-size:18px;color:var(--orange)}
.products-rule{left:112px;top:706px;width:490px;height:2px;background:#dadada}
.product-grid{left:112px;top:721px;display:grid;grid-template-columns:repeat(6,69px);column-gap:14.5px;row-gap:12px}
.product{width:69px;height:69px;background:#fff;border:1px solid #e0e0e0;padding:4px}
.product div{width:100%;height:100%}
.tone-a{background:linear-gradient(#3a3a3a,#9a9a8a 55%,#2a2a2a)}
.tone-b{background:linear-gradient(135deg,#f1efe9,#c8a08a)}
.tone-c{background:linear-gradient(135deg,#d89a7a,#b8614a)}
.tone-d{background:linear-gradient(#d3c4a6,#b9b3a5)}
.tone-e{background:linear-gradient(#1f2230,#c9c9cf)}
.products-divider{left:620px;top:725px;width:1px;height:134px;background:#d4d4d4}
.section-rule{left:237px;top:892px;width:528px;height:1px;background:#d2d2d2}

/* readers */
.readers{left:113px;top:912px;width:576px;height:204px;background:var(--orange);border-radius:3px 0 0 3px;box-shadow:0 3px 6px rgba(0,0,0,.12)}
.readers-title{left:15px;top:7px;font-family:"Oswald",sans-serif;font-size:18px;color:#fff}
.readers-all{right:20px;top:11px;font-family:"Oswald",sans-serif;font-size:12.5px;color:#fff}
.readers-rule{left:14px;top:36px;width:550px;height:1px;background:rgba(255,255,255,.45)}
.readers-split{left:278px;top:52px;width:1px;height:136px;background:rgba(255,255,255,.35)}
.reader{width:230px;font-family:"Roboto Condensed",sans-serif;color:#fff;font-size:9px;line-height:11.7px}
.reader .photo{float:left;width:80px;height:76px;margin:0 5px 0 0;border:1px solid rgba(255,255,255,.6)}
.reader h3{font-family:"Oswald",sans-serif;font-weight:400;font-size:14px;line-height:18px}
.reader .role{margin-bottom:6px}
.photo-man-a{background:linear-gradient(#8a8278,#4a3b33)}
.photo-man-b{background:linear-gradient(#6e7a86,#2d3640)}
.top-psychics{left:690px;top:912px;width:222px;height:204px;background:#fff;border:1px solid #e4e4e4;padding:0 14px}
.top-psychics h2{font-family:"Oswald",sans-serif;font-weight:400;font-size:18px;color:var(--grey-head);margin-top:9px;padding-bottom:4px;border-bottom:1px solid #d6d6d6}
.top-card{margin-top:18px;font-family:"Roboto Condensed",sans-serif;font-size:9px;line-height:11.7px;color:#888}
.top-card .photo{float:left;width:84px;height:77px;margin-right:9px;background:linear-gradient(#bcd3e4,#e9dccd)}
.top-card h3{font-family:"Oswald",sans-serif;font-weight:400;font-size:14px;color:#999;line-height:18px;margin-top:-3px}
.top-card .role{margin-bottom:6px}
.top-btn{left:822px;top:1078px;width:76px;height:26px;font-size:14px;line-height:24px}

/* footer */
.footer{left:0;top:1154px;width:1024px;height:46px;background:var(--footer);font-family:"Roboto Condensed",sans-serif;font-size:9.5px;color:#fff}
.footer-links{left:112px;top:16px}
.footer-copy{right:112px;top:18px}
</style>
</head>
<body>

<header>
  <div class="abs brand">
    <div class="brand-name">Lantern of Seers</div>
    <div class="brand-tag">a world of psychics</div>
  </div>
  <nav class="abs main-nav"><span>PSYCHIC</span><span class="sep"></span><span>MARKETPLACE</span><span class="sep"></span><span>MY ACCOUNT</span></nav>
  <div class="abs search"><div class="search-field">Search Now....</div><div class="search-btn">SEARCH</div></div>
</header>

<section class="abs hero" role="img" aria-label="Photo collage of smiling psychic readers"></section>
<div class="abs hero-banner"></div>
<div class="abs hero-kicker">MEET OUR</div>
<div class="abs hero-title">EXPERT LANTERN SEER</div>

<section class="abs welcome">
  <h1>WELCOME TO LANTERN OF SEERS</h1>
  <p>If you have an issue in your life that is causing you any sort of distress, no matter what it is, a reading from one of our psychics will give you immediate, compassionate insight. There are moments when you need more answers than you can get on your own. That's why the gifted psychics at Lantern of Seers are here for you, 24/7.</p>
  <p>Maybe your relationship suddenly fell apart and you don't know why. Perhaps you just lost a loved one and want to contact them. Maybe you suffered an unexpected financial crisis and you need to make a critical decision.</p>
</section>

<svg class="abs orange-side" width="272" height="363" viewBox="0 0 272 363" aria-hidden="true">
  <defs><linearGradient id="og" x1="0" y1="0" x2="0" y2="1"><stop offset="0" stop-color="#f5701f"/><stop offset="1" stop-color="#e8520a"/></linearGradient></defs>
  <path d="M0,136 L75,136 C92,62 150,6 236,0 L266,0 Q272,0 272,6 L272,338 Q272,363 248,363 L24,363 Q0,363 0,338 Z" fill="url(#og)"/>
</svg>
<div class="abs join-title">ARE YOU<br>PSYCHIC</div>
<div class="abs btn-light join-btn">JOIN NOW!</div>
<div class="abs mails-title">FIND DAILY MAILS</div>
<div class="abs mails-rule"></div>
<div class="abs mails-sub">Get New &amp; Exciting trends &amp; Ideas in your Inbox.</div>
<div class="abs mails-field">Enter Your Email...</div>
<div class="abs btn-light mails-btn">SIGNUP</div>

<div class="abs products-title">PRODUCTS</div>
<div class="abs products-rule"></div>
<div class="abs product-grid">
  <div class="product"><div class="tone-a" role="img" aria-label="Framed sign product"></div></div>
  <div class="product"><div class="tone-b" role="img" aria-label="Beaded bracelet product"></div></div>
  <div class="product"><div class="tone-c" role="img" aria-label="Patterned blouse product"></div></div>
  <div class="product"><div class="tone-d" role="img" aria-label="Long dress product"></div></div>
  <div class="product"><div class="tone-e" role="img" aria-label="Gown with banner product"></div></div>
  <div class="product"><div class="tone-a" role="img" aria-label="Framed sign product"></div></div>
  <div class="product"><div class="tone-d" role="img" aria-label="Long dress product"></div></div>
  <div class="product"><div class="tone-e" role="img" aria-label="Gown with banner product"></div></div>
  <div class="product"><div class="tone-a" role="img" aria-label="Framed sign product"></div></div>
  <div class="product"><div class="tone-b" role="img" aria-label="Beaded bracelet product"></div></div>
  <div class="product"><div class="tone-c" role="img" aria-label="Patterned blouse product"></div></div>
  <div class="product"><div class="tone-a" role="img" aria-label="Framed sign product"></div></div>
</div>
<div class="abs products-divider"></div>
<div class="abs section-rule"></div>

<section class="abs readers">
  <div class="abs readers-title">PSYCHIC READERS</div>
  <div class="abs readers-all">Veiw All...</div>
  <div class="abs readers-rule"></div>
  <div class="abs readers-split"></div>
  <article class="abs reader" style="left:17px;top:44px">
    <div class="photo photo-man-a" role="img" aria-label="Portrait of psychic reader Marcus Ellery"></div>
    <h3>Marcus Ellery</h3>
    <div class="role">Product Owner,<br>Northfold Insights</div>
    Lorem Ipsum is simply dummy text of the printing and typesetting industry. Lorem Ipsum has been the industry's standard dummy text ever since the 1500s, when an unknown printer took a galley of type and scrambled it to make a type specimen book. It has survived not only five centuries, but also the leap into electronic typesetting, remaining essentially unchanged.
  </article>
  <article class="abs reader" style="left:324px;top:44px">
    <div class="photo photo-man-b" role="img" aria-label="Portrait of psychic reader Owen Haldane"></div>
    <h3>Owen Haldane</h3>
    <div class="role">CEO and<br>Founder</div>
    Lorem Ipsum is simply dummy text of the printing and typesetting industry. Lorem Ipsum has been the industry's standard dummy text ever since the 1500s, when an unknown printer took a galley of type and scrambled it to make a type specimen book. It has survived not only five centuries, but also the leap into electronic typesetting, remaining essentially unchanged.
  </article>
</section>

<section class="abs top-psychics">
  <h2>TOP PSYCHICS</h2>
  <article class="top-card">
    <div class="photo" role="img" aria-label="Portrait of top psychic Brianna"></div>
    <h3>Brianna</h3>
    <div class="role">CEO and Founder</div>
    Lorem Ipsum is simply dummy text of the printing and typesetting industry. Lorem Ipsum the industry's standard dummy text ever since the 1500s, when an unknown printer
  </article>
</section>
<div class="abs btn-light top-btn">SIGNUP</div>

<footer class="abs footer">
  <div class="abs footer-links">About Psychic Readings | Contact us | Privacy Policy | Terms &amp; Conditions</div>
  <div class="abs footer-copy">Copyright 2013 Lantern of Seers (ACN 318 402 567). Trademark Lantern of Seers</div>
</footer>

</body>
</html>
```